Professional/modern business card design for construction company

We need a new business card design, double sided keeping it modern, sleek, professional and simple. We are an earthmoving business but do not want any pictures of machinery. I would like one side to have the logo and the other to have all the information, keeping with the colors in our logo. The business card will need to be able to be customised so we can use it for several different managers., we would also like to be able to use the design to apply it to other stationary ie. letterheads, notebooks etc. We do not really have a tag line but we could put on there that we specialise in - Agriculture, Civil Construction and Mining.

Contact Information for Business Card

Brolga Ridge Excavations Pty Ltd
ABN 58 402 937 615
82 Gumleaf Creek Road, Moree NSW 2400

Harold Benton
Managing Director
P 0418 639 204
E haroldbenton@brolgaridgeexc.com.au

Font styles to use
Serif
Sans Serif

Requirements
Nice to have
• I have attached some examples of ideas.
Should not have
• images of machinery

```html
<!DOCTYPE html>
<html lang="en">
<head>
<meta charset="utf-8">
<title>Brolga Ridge Excavations – Business Card</title>
<link rel="stylesheet" href="https://fonts.googleapis.com/css2?family=Anton&family=Montserrat:wght@500;600;700;800&display=swap">
<style>
  :root {
    --orange: #ef5a1f;
    --orange-deep: #c8461a;
    --orange-soft: #f7a27a;
    --peach: #fdebe1;
    --paper: #fffaf7;
    --ink: #2b2b2b;
    --backdrop: #e4e4e6;
  }
  * { margin: 0; padding: 0; box-sizing: border-box; }
  html, body { width: 1200px; height: 900px; overflow: hidden; }
  body {
    background: var(--backdrop);
    font-family: "Montserrat", sans-serif;
    color: var(--ink);
    position: relative;
  }
  .card {
    position: absolute;
    left: 285px;
    width: 630px;
    height: 360px;
    background: linear-gradient(115deg, var(--paper) 0%, #ffffff 40%, var(--peach) 100%);
    box-shadow: 0 10px 28px rgba(0,0,0,.18);
    overflow: hidden;
  }
  .card--front { top: 55px; }
  .card--back { top: 480px; }
  .card__bands { position: absolute; inset: 0; width: 100%; height: 100%; }

  /* Front side */
  .person {
    position: absolute; left: 42px; top: 52px;
  }
  .person__name {
    font-family: "Anton", sans-serif;
    font-size: 60px;
    line-height: 1;
    letter-spacing: 1px;
    text-transform: uppercase;
    color: var(--ink);
  }
  .person__surname { color: var(--orange); }
  .person__role {
    display: inline-block;
    margin-top: 8px;
    padding: 7px 44px 7px 16px;
    background: var(--orange);
    color: #fff;
    font-weight: 700;
    font-size: 17px;
    letter-spacing: 1.5px;
    text-transform: uppercase;
    clip-path: polygon(0 0, 100% 0, calc(100% - 18px) 100%, 0 100%);
  }
  .contacts {
    position: absolute; left: 42px; top: 200px;
    list-style: none;
  }
  .contacts__item {
    display: flex; align-items: center; gap: 14px;
    font-size: 15px; font-weight: 500;
    margin-bottom: 12px;
  }
  .contacts__icon {
    width: 24px; height: 24px; border-radius: 50%;
    background: var(--orange);
    display: flex; align-items: center; justify-content: center;
  }
  .front-brand {
    position: absolute; right: 34px; bottom: 22px;
    font-weight: 800; font-size: 15px; letter-spacing: .5px;
    color: var(--ink);
    text-transform: uppercase;
  }

  /* Back side */
  .brand {
    position: absolute; left: 0; right: 0; top: 118px;
    text-align: center;
  }
  .brand__name {
    display: inline-flex; align-items: center; gap: 12px;
    font-weight: 800; font-size: 26px; letter-spacing: 1px;
    text-transform: uppercase; color: var(--ink);
  }
  .brand__square { width: 22px; height: 22px; background: var(--orange); }
  .brand__details {
    margin-top: 14px;
    font-weight: 600; font-size: 12px; letter-spacing: 2.5px;
    text-transform: uppercase; line-height: 1.7;
  }
</style>
</head>
<body>

  <section class="card card--front" aria-label="Business card, contact side">
    <svg class="card__bands" viewBox="0 0 630 360" aria-hidden="true">
      <defs>
        <linearGradient id="band-front" x1="0" y1="0" x2="1" y2="0">
          <stop offset="0" stop-color="#ef5a1f" stop-opacity=".15"/>
          <stop offset=".35" stop-color="#ef5a1f"/>
          <stop offset="1" stop-color="#c8461a"/>
        </linearGradient>
      </defs>
      <polygon points="380,0 630,0 630,62 520,62 490,32 410,32" fill="url(#band-front)"/>
      <polygon points="630,62 520,62 490,32 630,32" fill="#ffffff" opacity=".35"/>
      <polygon points="250,290 430,290 460,262 630,262 630,360 230,360" fill="url(#band-front)"/>
    </svg>

    <div class="person">
      <h1 class="person__name">Harold <span class="person__surname">Benton</span></h1>
      <p class="person__role">Managing Director</p>
    </div>

    <ul class="contacts">
      <li class="contacts__item">
        <span class="contacts__icon">
          <svg width="13" height="13" viewBox="0 0 24 24" fill="#fff" aria-hidden="true"><path d="M6.6 10.8a15.1 15.1 0 0 0 6.6 6.6l2.2-2.2c.3-.3.7-.4 1-.2 1.1.4 2.3.6 3.6.6.6 0 1 .4 1 1V20c0 .6-.4 1-1 1A17 17 0 0 1 3 4c0-.6.4-1 1-1h3.5c.6 0 1 .4 1 1 0 1.3.2 2.5.6 3.6.1.3 0 .7-.2 1z"/></svg>
        </span>
        0418 639 204
      </li>
      <li class="contacts__item">
        <span class="contacts__icon">
          <svg width="13" height="13" viewBox="0 0 24 24" fill="#fff" aria-hidden="true"><path d="M3 5h18v14H3z M3 5l9 7 9-7" stroke="#ef5a1f" stroke-width="1.5"/></svg>
        </span>
        haroldbenton@brolgaridgeexc.com.au
      </li>
    </ul>

    <p class="front-brand">Brolga Ridge Excavations</p>
  </section>

  <section class="card card--back" aria-label="Business card, company side">
    <svg class="card__bands" viewBox="0 0 630 360" aria-hidden="true">
      <defs>
        <linearGradient id="band-back" x1="0" y1="0" x2="1" y2="0">
          <stop offset="0" stop-color="#ef5a1f" stop-opacity=".15"/>
          <stop offset=".4" stop-color="#ef5a1f"/>
          <stop offset="1" stop-color="#c8461a"/>
        </linearGradient>
      </defs>
      <polygon points="150,0 630,0 630,34 200,34" fill="url(#band-back)" opacity=".9"/>
      <polygon points="300,330 470,330 500,300 630,300 630,360 280,360" fill="url(#band-back)"/>
      <polygon points="330,270 560,270 580,250 630,250 630,284 350,284" fill="url(#band-back)" opacity=".55"/>
    </svg>

    <div class="brand">
      <p class="brand__name"><span class="brand__square"></span>Brolga Ridge Excavations</p>
      <p class="brand__details">82 Gumleaf Creek Road, Moree NSW 2400<br>ABN 58 402 937 615</p>
    </div>
  </section>

</body>
</html>
```